Fox & Fern honey company needs a label design.

We need a label design for a new honey company, based in the state of Florida called 'Fox & Fern". We are supplying our online customers with the highest quality of the various kinds of raw honey. Our product is honey in the oval hexagon glass jar with black lid. We would like to see designs that use black background with gold font .
In the upper part of the label is gold flying Honey Bee (profile, silhouette). The name of the brand "Fox & Fern" - Caramel font. Additional fonts are Cinzel, Source Sans Pro. Label measurements 2.6" by 3".
Label content:
Fox & Fern
RAW HONEY
wildflower
PURE & NATURAL
made by Florida Bees
foxandfernhoney.com
NET WT 12oz (340g)

The final design should have eye catching, luxurious look.
Updates

Target Market(s)

Luxury

Industry/Entity Type

Food (bee products)

Other font styles liked:
• caramel

Colors

Designer to choose colors to be used in the design.

Requirements
Must have
• Gold letters on black background, Drawing of a bee, flying in profile

```html
<!DOCTYPE html>
<html lang="en">
<head>
<meta charset="utf-8">
<title>Fox &amp; Fern Raw Honey Label</title>
<link href="https://fonts.googleapis.com/css2?family=Source+Sans+3:wght@400;600&display=swap" rel="stylesheet">
<style>
  :root {
    --backdrop: #f1e6d8;
    --label-black: #0d0d0d;
    --label-edge: #1e1e1e;
    --gold: #c4952f;
    --gold-light: #e2b451;
    --gold-dark: #8a6420;
  }
  * { box-sizing: border-box; margin: 0; padding: 0; }
  html, body {
    width: 893px;
    height: 1200px;
    overflow: hidden;
    background: var(--backdrop);
  }
  .canvas {
    width: 893px;
    height: 1200px;
    display: flex;
    align-items: center;
    justify-content: center;
  }
  .label {
    width: 780px;
    height: 900px;
    background: linear-gradient(90deg, var(--label-edge) 0%, var(--label-black) 50%, var(--label-edge) 100%);
    display: flex;
    flex-direction: column;
    align-items: center;
    padding-top: 90px;
    color: var(--gold);
    font-family: "Source Sans 3", sans-serif;
    text-align: center;
  }
  .brand-name {
    font-size: 92px;
    font-weight: 400;
    line-height: 1;
    color: var(--gold);
    letter-spacing: 1px;
  }
  .bee-illustration {
    margin-top: 40px;
    width: 200px;
    height: 120px;
    border-radius: 50%;
    background: radial-gradient(ellipse at center, var(--gold-light) 0%, var(--gold) 35%, var(--gold-dark) 60%, transparent 72%);
  }
  .product-type {
    margin-top: 50px;
    font-size: 54px;
    font-weight: 400;
    letter-spacing: 5px;
    line-height: 1;
  }
  .variety {
    margin-top: 12px;
    font-size: 52px;
    font-weight: 400;
    letter-spacing: 1px;
    line-height: 1;
  }
  .claim {
    margin-top: 58px;
    font-size: 60px;
    font-weight: 400;
    letter-spacing: 2px;
    line-height: 1;
  }
  .website {
    margin-top: 22px;
    font-size: 40px;
    line-height: 1;
  }
  .origin {
    margin-top: 18px;
    font-size: 34px;
    line-height: 1;
  }
  .net-weight {
    margin-top: 28px;
    font-size: 29px;
    line-height: 1;
  }
</style>
</head>
<body>
  <main class="canvas">
    <section class="label">
      <h1 class="brand-name">Fox &amp; Fern</h1>
      <div class="bee-illustration" role="img" aria-label="Gold engraved honey bee flying in profile"></div>
      <p class="product-type">RAW HONEY</p>
      <p class="variety">wildflower</p>
      <p class="claim">PURE &amp; NATURAL</p>
      <p class="website">foxandfernhoney.com</p>
      <p class="origin">Made by Florida Bees</p>
      <p class="net-weight">NET WT 12oz (340g)</p>
    </section>
  </main>
</body>
</html>
```